NURSING: STEP BEYOND THE HEDGEROW

Size of the book cover: 140 x 215 mms

I need a cover for the 30,000 word book I have just written. It is a positive take on what I think nursing is and what it needs to be in the future. It is also my story of being nursed and of being a nurse.

My dream is that nurses honor themselves; that they look to the future with confidence and intelligence and that care continues to be delivered with compassionate person centeredness.

I define nursing as a professional workforce which, with probity, prevent or relieve distress; provide compassionate, safe, excellent care; and which contributes to the organization of healthcare.

The name comes from a Biblical parable Mathew 5:14-16. If a light is hidden under a bushel (basket) it is barely seen. If it is lit out from the basket it is clearly seen. As nurses we must continue to take up our mantel and ensure our light is seen and that it continues to shine the way we want it to.

As nurses we each take up our own lantern of caring, each in our own ways. To walk more brightly in our own paths of service.

The final design should show the specialness of nursing.

Target Market(s)

Nurses present, past and future

Industry/Entity Type

Healthcare

Font styles to use
Sans Serif
Other font styles liked:
• Whatever you think will suit

Colors
ec1f27
0393ce
9bcb3c

Requirements
Must have
• Be friendly, calming.
• NB: I am not sure whether the title should be in uppercase or not. Nursing could be uppercase and step beyond the hedgerow could be lower case. I leave it to you experienced people
Nice to have
• Something that depicts nursing...or is suggestive of nursing and the specialness of the work we do. How we bring our light to our patients as we 'hold them in the palms of out hands' and care for them. How they honor us by allowing us into their lives. Our rich past and out history allows us to be who we are today and we look to the future with confidence and hope
• I like rich colors, eg the color type you might find on a stained glass window in a church - rich emerald green or rich crimson red or the deep blue of a nurses cape
Should not have
• A dark cover
• clutter
• Religious overtone
• I have chosen three colors but they are not in the shading I would like - see above

```html
<!DOCTYPE html>
<html lang="en">
<head>
<meta charset="utf-8">
<title>Nursing: Step Beyond the Hedgerow – Cover Wrap</title>
<link rel="stylesheet" href="https://fonts.googleapis.com/css2?family=Lato:ital,wght@0,300;0,400;0,700;0,900;1,400&family=Rubik:wght@400;500;700;900&display=swap">
<style>
  :root {
    --page-bg: #e9e9e9;
    --charcoal: #373737;
    --charcoal-deep: #2c2c2c;
    --leaf: #9bcb3c;
    --leaf-deep: #7fb53a;
    --leaf-pale: #b9dd86;
    --meadow: #6fa84a;
    --cape-blue: #1a9bd7;
    --cape-blue-deep: #1590ca;
    --ink: #26312a;
    --paper: #ffffff;
    --author-grey: #cfcfcf;
  }
  * { box-sizing: border-box; margin: 0; padding: 0; }
  html, body {
    width: 1200px; height: 850px; overflow: hidden;
    background: var(--page-bg);
  }
  .cover-wrap {
    position: absolute; left: 153px; top: 105px;
    width: 894px; height: 640px;
    display: flex;
    box-shadow: 0 6px 24px rgba(0,0,0,0.12);
  }

  /* ---------- back cover ---------- */
  .back-cover {
    position: relative; width: 417px; height: 640px;
    background: var(--cape-blue);
    color: var(--paper);
  }
  .back-blurb {
    padding: 44px 30px 0 30px;
    font-family: "Lato", sans-serif;
    font-style: italic;
    font-size: 9px; line-height: 1.5;
    text-align: justify;
  }
  .back-blurb p { margin-bottom: 11px; }
  .back-dedication {
    position: absolute; left: 0; right: 0; bottom: 0; height: 38px;
    background: var(--leaf);
    display: flex; align-items: center; padding-left: 150px;
    font-family: "Rubik", sans-serif; font-size: 10px; color: var(--paper);
  }

  /* ---------- spine ---------- */
  .spine {
    position: relative; width: 60px; height: 640px;
    background: var(--cape-blue-deep);
    color: var(--paper);
    border-left: 1px solid rgba(0,0,0,0.08);
    border-right: 1px solid rgba(0,0,0,0.08);
  }
  .spine-title {
    position: absolute; top: 26px; left: 50%; transform: translateX(-50%);
    writing-mode: vertical-rl;
    display: flex; align-items: center; gap: 10px;
    white-space: nowrap;
  }
  .spine-title-main {
    font-family: "Rubik", sans-serif; font-weight: 900;
    font-size: 34px; letter-spacing: 1px;
  }
  .spine-title-sub {
    font-family: "Rubik", sans-serif; font-weight: 500;
    font-size: 7px; letter-spacing: 1px; text-transform: uppercase;
  }
  .spine-author {
    position: absolute; bottom: 52px; left: 50%; transform: translateX(-50%);
    writing-mode: vertical-rl; white-space: nowrap;
    font-family: "Lato", sans-serif; font-size: 11px;
  }
  .spine-author strong { font-weight: 900; }
  .spine-band {
    position: absolute; left: 0; right: 0; bottom: 0; height: 38px;
    background: var(--leaf-deep);
  }

  /* ---------- front cover ---------- */
  .front-cover {
    position: relative; width: 417px; height: 640px; overflow: hidden;
    background: linear-gradient(to bottom,
      var(--charcoal-deep) 0px, var(--charcoal) 122px,
      var(--leaf) 140px, var(--leaf-pale) 230px);
  }
  .front-author {
    position: absolute; top: 26px; left: 16px;
    font-family: "Lato", sans-serif; font-size: 13px; letter-spacing: 0.5px;
    color: var(--author-grey);
  }
  .front-author .surname { color: var(--paper); font-weight: 900; }
  .front-title {
    position: absolute; top: 84px; left: 10px; right: 8px;
    font-family: "Rubik", sans-serif; white-space: nowrap;
  }
  .front-title-main {
    display: block;
    font-weight: 900; font-size: 80px; line-height: 1;
    color: var(--leaf);
  }
  .front-title-sub {
    display: block; text-align: right; margin-right: 14px; margin-top: 4px;
    font-weight: 500; font-size: 7.5px; letter-spacing: 1px;
    text-transform: uppercase; color: var(--ink);
  }
  .front-quote {
    position: absolute; top: 192px; left: 50px; right: 14px;
    text-align: center;
    font-family: "Rubik", sans-serif; font-size: 15px; line-height: 1.3;
    color: var(--ink);
  }
  .front-quote strong { font-weight: 700; }
  .front-landscape {
    position: absolute; left: 0; right: 0; top: 262px; bottom: 38px;
    background: linear-gradient(to bottom, var(--leaf-pale), var(--meadow));
  }
  .front-foreword {
    position: absolute; left: 0; right: 0; bottom: 0; height: 38px;
    background: var(--leaf);
    display: flex; align-items: center; justify-content: flex-end;
    padding-right: 16px;
    font-family: "Rubik", sans-serif; font-size: 11px; color: var(--ink);
  }
</style>
</head>
<body>
  <div class="cover-wrap">

    <section class="back-cover">
      <div class="back-blurb">
        <p>This book is written the way it is told here. It is the work of a person who has lived nursing all her life, and it is shared with honesty and candour. There is something for everyone to take from it, and nurses will see themselves mirrored in the many anecdotes and stories.</p>
        <p>Nursing: step beyond the hedgerow is a book which brings into the light the rich and varied work of nursing. Through its words it gently challenges nurses to think deeply about what being a nurse means to them.</p>
        <p>Nursing is a big deal. Nurses choose to be nurses. No one tells them they must; they have a reason they decide to. The people they care for honour them by letting them into their lives at what can be the most vulnerable and dramatic times. How nurses walk with their patients has consequences for those in their care and for themselves.</p>
        <p>One of the realities is that the work crosses normal social boundaries. It is seldom talked about outside of nursing, yet the support nurses give each other is vital in keeping them healthy and able.</p>
        <p>A lantern of caring was lit long ago, and that lantern continues to glow. It is relit every moment by nurses around the world as they go about their work.</p>
        <p>This is not just a story of nursing. It is the story of a professional life, told through personal accounts and experiences. It also offers thoughts on nursing now and into the future, with its many new challenges and opportunities. The future is in nurses' hands, and they can look to it with confidence.</p>
      </div>
      <div class="back-dedication">For nurses everywhere.</div>
    </section>

    <section class="spine">
      <div class="spine-title">
        <span class="spine-title-main">NURSING</span>
        <span class="spine-title-sub">step beyond the hedgerow</span>
      </div>
      <div class="spine-author">Maren <strong>Colby</strong></div>
      <div class="spine-band"></div>
    </section>

    <section class="front-cover">
      <div class="front-author">MAREN <span class="surname">COLBY</span></div>
      <h1 class="front-title">
        <span class="front-title-main">NURSING</span>
        <span class="front-title-sub">step beyond the hedgerow</span>
      </h1>
      <p class="front-quote">“We each take up our own lantern of <strong>CARING</strong>, each in our own ways, to walk more brightly in our own path of service”</p>
      <div class="front-landscape" role="img" aria-label="Photograph of a green mountain valley with forest and meadow"></div>
      <div class="front-foreword">Foreword by Ruth Ashdown RN</div>
    </section>

  </div>
</body>
</html>
```